Designing of Orientation Materials and Innovative Ways to ‘Market’ Procurement Function

To Market and promote Procurement function and it’s ‘real’ capabilities clearly, to demonstrate that the function is an enabler instead being perceive as a barrier to other internal functions. Sometimes due to the lack of a common language even makes it difficult for other functions (e.g) Marketing and Procurement to understand each other’s aims and intentions.
The audience could be from all functions such as; Human Resource, Finance, Sales & Marketing, Supply Chain/Procurement, Corporate Affairs and Information System.

```html
<!DOCTYPE html>
<html lang="en">
<head>
<meta charset="utf-8">
<title>Procurement's Evolving Value Proposition</title>
<link href="https://fonts.googleapis.com/css2?family=Source+Sans+3:wght@400;600;700&display=swap" rel="stylesheet">
<style>
  :root {
    --backdrop: #e8e8e8;
    --slide: #ffffff;
    --brand-blue: #1476c0;
    --navy: #2a2060;
    --tier-top: #74cff2;
    --tier-two: #1eb8e2;
    --tier-three: #1f9dd0;
    --tier-base: #1684bd;
    --arrow: #77d0f2;
    --desc-blue: #1a7fc1;
  }
  html, body {
    margin: 0;
    padding: 0;
    width: 1200px;
    height: 1200px;
    overflow: hidden;
    background: var(--backdrop);
    font-family: "Source Sans 3", "Source Sans Pro", sans-serif;
  }
  .slide {
    position: absolute;
    left: 110px;
    top: 299px;
    width: 980px;
    height: 601px;
    background: var(--slide);
  }
  .slide-title {
    position: absolute;
    left: 302px;
    top: 324px;
    width: 610px;
    height: 42px;
    border-radius: 13px;
    background: var(--brand-blue);
    color: #fff;
    font-weight: 700;
    font-size: 25px;
    line-height: 43px;
    text-align: center;
    letter-spacing: 0.4px;
    margin: 0;
  }
  .diagram {
    position: absolute;
    left: 0;
    top: 0;
    width: 1200px;
    height: 1200px;
  }
  .tier-label {
    font-family: "Source Sans 3", "Source Sans Pro", sans-serif;
    font-weight: 700;
    font-size: 16px;
    fill: var(--navy);
    text-anchor: middle;
    letter-spacing: 0.3px;
  }
  .arrow-label {
    font-family: "Source Sans 3", "Source Sans Pro", sans-serif;
    font-weight: 400;
    font-size: 13.5px;
    fill: #fff;
    text-anchor: middle;
  }
  .benefit {
    position: absolute;
    right: 157px;
    margin: 0;
    text-align: right;
    font-size: 16px;
    line-height: 20.5px;
  }
  .benefit strong { font-weight: 700; }
  .benefit--blue { color: var(--desc-blue); }
  .benefit--navy { color: var(--navy); }
</style>
</head>
<body>
  <div class="slide"></div>
  <h1 class="slide-title">PROCUREMENT’S EVOLVING VALUE PROPOSITION</h1>

  <svg class="diagram" viewBox="0 0 1200 1200" xmlns="http://www.w3.org/2000/svg">
    <g class="tier-shadows" fill="#f2f2f2">
      <polygon points="530,599 645,574 660,576 565,604"/>
      <polygon points="440,686 694,660 700,662 580,690"/>
      <polygon points="350,772 744,745 750,747 600,776"/>
    </g>

    <polygon class="tier tier-top" points="555,415 645,572 464,572" fill="var(--tier-top)"/>
    <polygon class="tier tier-two" points="433,604 664,604 694,658 414,658" fill="var(--tier-two)"/>
    <polygon class="tier tier-three" points="387,689 714,689 744,743 365,743" fill="var(--tier-three)"/>
    <polygon class="tier tier-base" points="345,775 763,775 798,837 311,837" fill="var(--tier-base)"/>

    <text class="tier-label" x="555" y="527">TOTAL</text>
    <text class="tier-label" x="555" y="548">ENTERPRICE</text>
    <text class="tier-label" x="557" y="628">SUPPLIER RELATIONSHIP</text>
    <text class="tier-label" x="557" y="649">MANAGEMENT</text>
    <text class="tier-label" x="553" y="714">STRATEGIC SOURCING AND CATEGORY</text>
    <text class="tier-label" x="553" y="735">MANAGEMENT</text>
    <text class="tier-label" x="555" y="812">AP TRANSACTIONAL EFFICIENCIES</text>

    <g class="growth-arrow" transform="translate(394,618) rotate(-59.6)">
      <line x1="0" y1="0" x2="196" y2="0" stroke="var(--arrow)" stroke-width="24" stroke-linecap="round"/>
      <polygon points="190,-21 222,0 190,21" fill="var(--arrow)"/>
      <text class="arrow-label" x="118" y="5">Enhance Margins</text>
    </g>

    <g class="growth-arrow" transform="translate(267,829) rotate(-58.9)">
      <line x1="0" y1="0" x2="152" y2="0" stroke="var(--arrow)" stroke-width="24" stroke-linecap="round"/>
      <polygon points="146,-21 178,0 146,21" fill="var(--arrow)"/>
      <text class="arrow-label" x="72" y="5">Deliver Savings</text>
    </g>
  </svg>

  <p class="benefit benefit--blue" style="top:457px;"><strong>Global interests</strong> sought to capture cross<br>business benefits above individual interests</p>
  <p class="benefit benefit--blue" style="top:604px;"><strong>Competitive advantage</strong> through supplier<br>collaboration to drive innovation annd growth</p>
  <p class="benefit benefit--navy" style="top:692px;"><strong>Improve total cost of ownership</strong><br>through optimisation of purchasing</p>
  <p class="benefit benefit--navy" style="top:782px;"><strong>Cost out</strong> through process<br>efficiency</p>
</body>
</html>
```